Calendar design with baby pictures

I need to get 2 calendars designed, one wall hanging A5 size and one table top. I want to use my baby pics on it in very creative way. On some months i just want to use one picture and on some i will want to use a collage of few pics. The design should allow me to place pictures myself later on as i dont want to upload so many pics here.

```html
<!DOCTYPE html>
<html lang="en">
<head>
<meta charset="utf-8">
<title>12 months Wall Calendar Poster 2015</title>
<link rel="stylesheet" href="https://fonts.googleapis.com/css2?family=Amatic+SC:wght@700&family=Cabin+Condensed:wght@500&family=Source+Sans+3:wght@400&display=swap">
<style>
:root{
  --page:#ffffff;
  --ink:#555555;
  --navy:#1f2c58;
  --navy-soft:#27366a;
  --teal:#1f8196;
  --purple:#5a3f88;
  --day:#222222;
  --blob-top:#ffffff;
  --blob-bottom:#e4e4e6;
  --frame-line:#d6d6d6;
}
*{margin:0;padding:0;box-sizing:border-box}
html,body{width:846px;height:1200px;overflow:hidden;background:var(--page)}
body{position:relative;font-family:"Cabin Condensed",sans-serif;color:var(--day)}
.sheet-title{position:absolute;top:58px;left:0;width:846px;text-align:center;font-family:"Source Sans 3",sans-serif;font-weight:400;font-size:28px;color:var(--ink);letter-spacing:.2px}
.poster{position:absolute;left:56px;top:125px;width:735px;height:1044px;border:1px solid var(--frame-line);overflow:hidden}
.poster-art{position:absolute;left:0;top:0}
.year-badge{position:absolute;left:320px;top:586px;width:66px;height:42px;border-radius:50% 46% 50% 44%;background:linear-gradient(var(--blob-top),var(--blob-bottom));box-shadow:0 2px 4px rgba(0,0,0,.25);font-family:"Amatic SC",sans-serif;font-size:30px;line-height:42px;text-align:center;color:#111}
.month{position:absolute;border-radius:48% 52% 44% 56% / 56% 46% 54% 44%;background:linear-gradient(160deg,var(--blob-top) 40%,var(--blob-bottom));box-shadow:2px 4px 6px rgba(0,0,0,.22);padding:24px 0 0 18px}
.month.label-below{padding-top:14px}
.weekdays{display:grid;grid-template-columns:repeat(7,19px);font-size:10px;height:13px;line-height:13px}
.weekdays span{text-align:center}
.weekdays .sun{color:var(--purple)}
.weekdays .sat{color:var(--teal)}
.days{display:grid;grid-template-columns:repeat(7,19px);grid-auto-rows:13.5px;font-size:11.5px;line-height:13px}
.days span{text-align:center}
.days span:nth-child(7n+1):not(:empty),
.days span:nth-child(7n):not(:empty){color:#fff;border-radius:50%;width:13px;height:13px;margin:0 auto;font-size:9.5px;line-height:13px}
.days span:nth-child(7n+1):not(:empty){background:var(--purple)}
.days span:nth-child(7n):not(:empty){background:var(--teal)}
.month-name{position:absolute;font-family:"Amatic SC",sans-serif;font-size:27px;line-height:30px;height:30px;color:#fff;text-align:center;border-radius:45% 50% 40% 55% / 60% 50% 50% 40%;box-shadow:1px 2px 3px rgba(0,0,0,.25);z-index:2}
.month-name.teal{background:var(--teal)}
.month-name.purple{background:var(--purple)}
.month-name.vertical{writing-mode:vertical-rl;transform:rotate(180deg);width:30px;height:72px;line-height:30px}
.owl-frame{fill:var(--navy-soft);stroke-width:2}
</style>
</head>
<body>
<h1 class="sheet-title">12 months / Wall Calendar Poster (1 pages)</h1>

<div class="poster">
  <svg class="poster-art" width="735" height="1044" viewBox="0 0 735 1044">
    <defs>
      <radialGradient id="owl-pink" cx="50%" cy="40%" r="60%"><stop offset="0" stop-color="#f6c4cb"/><stop offset="1" stop-color="#d9808e"/></radialGradient>
      <radialGradient id="owl-teal" cx="50%" cy="40%" r="60%"><stop offset="0" stop-color="#8fe0d4"/><stop offset="1" stop-color="#33a898"/></radialGradient>
      <radialGradient id="owl-green" cx="50%" cy="40%" r="60%"><stop offset="0" stop-color="#c9e67a"/><stop offset="1" stop-color="#7fae28"/></radialGradient>
      <radialGradient id="owl-purple" cx="50%" cy="40%" r="60%"><stop offset="0" stop-color="#b6a3d8"/><stop offset="1" stop-color="#705aa0"/></radialGradient>
      <radialGradient id="owl-orange" cx="50%" cy="40%" r="60%"><stop offset="0" stop-color="#ffd06a"/><stop offset="1" stop-color="#e9801c"/></radialGradient>
      <radialGradient id="owl-tan" cx="50%" cy="40%" r="60%"><stop offset="0" stop-color="#f4e7cf"/><stop offset="1" stop-color="#b48e5e"/></radialGradient>
      <radialGradient id="owl-sky" cx="50%" cy="40%" r="60%"><stop offset="0" stop-color="#a6e2ea"/><stop offset="1" stop-color="#3fa9bd"/></radialGradient>
      <radialGradient id="bird-blue" cx="50%" cy="50%" r="60%"><stop offset="0" stop-color="#b8e4f0"/><stop offset="1" stop-color="#5fb3cc"/></radialGradient>
    </defs>
    <path d="M0,0H735V545C650,520 560,600 470,585C420,578 400,560 360,560C300,560 260,520 180,520C100,520 50,540 0,530Z" fill="var(--navy)"/>

    <g class="owl-spots">
      <ellipse class="owl-frame" cx="52" cy="123" rx="58" ry="62" stroke="#e99aa6"/>
      <ellipse role="img" aria-label="Owl illustration with glasses" cx="46" cy="125" rx="42" ry="50" fill="url(#owl-pink)"/>

      <ellipse role="img" aria-label="Little bird illustration" cx="185" cy="92" rx="42" ry="20" fill="url(#bird-blue)"/>

      <ellipse class="owl-frame" cx="536" cy="119" rx="64" ry="76" stroke="#f29a9a"/>
      <ellipse role="img" aria-label="Teal owl illustration" cx="536" cy="116" rx="54" ry="64" fill="url(#owl-teal)"/>

      <ellipse class="owl-frame" cx="158" cy="270" rx="64" ry="68" stroke="#cfd8e8"/>
      <ellipse role="img" aria-label="Green owl illustration" cx="158" cy="270" rx="50" ry="58" fill="url(#owl-green)"/>

      <ellipse class="owl-frame" cx="4" cy="311" rx="44" ry="56" stroke="#e0604c"/>
      <ellipse role="img" aria-label="Purple owl illustration" cx="6" cy="311" rx="32" ry="44" fill="url(#owl-purple)"/>

      <ellipse class="owl-frame" cx="700" cy="296" rx="58" ry="66" stroke="#e0604c"/>
      <ellipse role="img" aria-label="Orange owl illustration" cx="704" cy="298" rx="44" ry="54" fill="url(#owl-orange)"/>

      <ellipse class="owl-frame" cx="579" cy="505" rx="58" ry="54" stroke="#f4e6dc"/>
      <ellipse role="img" aria-label="Tan owl illustration" cx="579" cy="507" rx="46" ry="44" fill="url(#owl-tan)"/>

      <ellipse class="owl-frame" cx="724" cy="467" rx="40" ry="66" stroke="#6fc4a8"/>
      <ellipse role="img" aria-label="Owl illustration at right edge" cx="726" cy="470" rx="28" ry="48" fill="url(#owl-sky)"/>

      <ellipse class="owl-frame" cx="4" cy="460" rx="30" ry="66" stroke="#6fc4a8"/>
      <ellipse role="img" aria-label="Snowman illustration" cx="4" cy="462" rx="18" ry="48" fill="url(#owl-sky)"/>
    </g>

    <rect role="img" aria-label="Baby photo in ornate frame" x="182" y="7" width="217" height="175" rx="18" fill="#d9c7b8" stroke="#f4e6dc" stroke-width="6"/>
    <ellipse role="img" aria-label="Baby photo in oval frame" cx="342" cy="303" rx="62" ry="95" fill="#b59a84" stroke="#f4e6dc" stroke-width="5"/>
    <rect role="img" aria-label="Baby photo in square frame" x="473" y="272" width="132" height="143" rx="10" fill="#d8b6a0" stroke="#e0604c" stroke-width="4"/>
    <ellipse role="img" aria-label="Baby photo in oval frame with small owl" cx="181" cy="441" rx="112" ry="69" fill="#7f7670" stroke="#e04a2e" stroke-width="4"/>
    <path role="img" aria-label="Baby photo in heart frame" d="M399,448C380,418 327,422 327,462C327,500 374,530 399,552C424,530 471,500 471,462C471,422 418,418 399,448Z" fill="#6a8a5a" stroke="#f4e6dc" stroke-width="4"/>
  </svg>

  <div class="year-badge">2015</div>
</div>

<div class="month-name teal" style="left:69px;top:745px;width:90px">January</div>
<div class="month" style="left:80px;top:752px;width:165px;height:110px">
  <div class="weekdays"><span class="sun">sun</span><span>mon</span><span>tue</span><span>wed</span><span>thu</span><span>fri</span><span class="sat">sat</span></div>
  <div class="days"><span></span><span></span><span></span><span></span><span>1</span><span>2</span><span>3</span><span>4</span><span>5</span><span>6</span><span>7</span><span>8</span><span>9</span><span>10</span><span>11</span><span>12</span><span>13</span><span>14</span><span>15</span><span>16</span><span>17</span><span>18</span><span>19</span><span>20</span><span>21</span><span>22</span><span>23</span><span>24</span><span>25</span><span>26</span><span>27</span><span>28</span><span>29</span><span>30</span><span>31</span></div>
</div>

<div class="month-name purple" style="left:246px;top:740px;width:100px">February</div>
<div class="month" style="left:252px;top:752px;width:165px;height:110px">
  <div class="weekdays"><span class="sun">sun</span><span>mon</span><span>tue</span><span>wed</span><span>thu</span><span>fri</span><span class="sat">sat</span></div>
  <div class="days"><span>1</span><span>2</span><span>3</span><span>4</span><span>5</span><span>6</span><span>7</span><span>8</span><span>9</span><span>10</span><span>11</span><span>12</span><span>13</span><span>14</span><span>15</span><span>16</span><span>17</span><span>18</span><span>19</span><span>20</span><span>21</span><span>22</span><span>23</span><span>24</span><span>25</span><span>26</span><span>27</span><span>28</span></div>
</div>

<div class="month-name teal" style="left:467px;top:730px;width:88px">March</div>
<div class="month" style="left:432px;top:752px;width:165px;height:110px">
  <div class="weekdays"><span class="sun">sun</span><span>mon</span><span>tue</span><span>wed</span><span>thu</span><span>fri</span><span class="sat">sat</span></div>
  <div class="days"><span>1</span><span>2</span><span>3</span><span>4</span><span>5</span><span>6</span><span>7</span><span>8</span><span>9</span><span>10</span><span>11</span><span>12</span><span>13</span><span>14</span><span>15</span><span>16</span><span>17</span><span>18</span><span>19</span><span>20</span><span>21</span><span>22</span><span>23</span><span>24</span><span>25</span><span>26</span><span>27</span><span>28</span><span>29</span><span>30</span><span>31</span></div>
</div>

<div class="month-name purple vertical" style="left:594px;top:765px">April</div>
<div class="month" style="left:614px;top:740px;width:170px;height:108px;padding-top:18px">
  <div class="weekdays"><span class="sun">sun</span><span>mon</span><span>tue</span><span>wed</span><span>thu</span><span>fri</span><span class="sat">sat</span></div>
  <div class="days"><span></span><span></span><span></span><span>1</span><span>2</span><span>3</span><span>4</span><span>5</span><span>6</span><span>7</span><span>8</span><span>9</span><span>10</span><span>11</span><span>12</span><span>13</span><span>14</span><span>15</span><span>16</span><span>17</span><span>18</span><span>19</span><span>20</span><span>21</span><span>22</span><span>23</span><span>24</span><span>25</span><span>26</span><span>27</span><span>28</span><span>29</span><span>30</span></div>
</div>

<div class="month-name teal" style="left:72px;top:860px;width:68px">May</div>
<div class="month" style="left:84px;top:872px;width:160px;height:124px;padding-top:30px">
  <div class="weekdays"><span class="sun">sun</span><span>mon</span><span>tue</span><span>wed</span><span>thu</span><span>fri</span><span class="sat">sat</span></div>
  <div class="days"><span></span><span></span><span></span><span></span><span></span><span>1</span><span>2</span><span>3</span><span>4</span><span>5</span><span>6</span><span>7</span><span>8</span><span>9</span><span>10</span><span>11</span><span>12</span><span>13</span><span>14</span><span>15</span><span>16</span><span>17</span><span>18</span><span>19</span><span>20</span><span>21</span><span>22</span><span>23</span><span>24</span><span>25</span><span>26</span><span>27</span><span>28</span><span>29</span><span>30</span><span>31</span></div>
</div>

<div class="month-name purple" style="left:312px;top:866px;width:85px">June</div>
<div class="month" style="left:254px;top:878px;width:160px;height:116px">
  <div class="weekdays"><span class="sun">sun</span><span>mon</span><span>tue</span><span>wed</span><span>thu</span><span>fri</span><span class="sat">sat</span></div>
  <div class="days"><span></span><span>1</span><span>2</span><span>3</span><span>4</span><span>5</span><span>6</span><span>7</span><span>8</span><span>9</span><span>10</span><span>11</span><span>12</span><span>13</span><span>14</span><span>15</span><span>16</span><span>17</span><span>18</span><span>19</span><span>20</span><span>21</span><span>22</span><span>23</span><span>24</span><span>25</span><span>26</span><span>27</span><span>28</span><span>29</span><span>30</span></div>
</div>

<div class="month-name teal" style="left:497px;top:850px;width:70px">July</div>
<div class="month" style="left:428px;top:866px;width:165px;height:116px">
  <div class="weekdays"><span class="sun">sun</span><span>mon</span><span>tue</span><span>wed</span><span>thu</span><span>fri</span><span class="sat">sat</span></div>
  <div class="days"><span></span><span></span><span></span><span>1</span><span>2</span><span>3</span><span>4</span><span>5</span><span>6</span><span>7</span><span>8</span><span>9</span><span>10</span><span>11</span><span>12</span><span>13</span><span>14</span><span>15</span><span>16</span><span>17</span><span>18</span><span>19</span><span>20</span><span>21</span><span>22</span><span>23</span><span>24</span><span>25</span><span>26</span><span>27</span><span>28</span><span>29</span><span>30</span><span>31</span></div>
</div>

<div class="month-name purple" style="left:634px;top:856px;width:95px">August</div>
<div class="month" style="left:604px;top:870px;width:172px;height:120px;padding-top:26px">
  <div class="weekdays"><span class="sun">sun</span><span>mon</span><span>tue</span><span>wed</span><span>thu</span><span>fri</span><span class="sat">sat</span></div>
  <div class="days"><span></span><span></span><span></span><span></span><span></span><span></span><span>1</span><span>2</span><span>3</span><span>4</span><span>5</span><span>6</span><span>7</span><span>8</span><span>9</span><span>10</span><span>11</span><span>12</span><span>13</span><span>14</span><span>15</span><span>16</span><span>17</span><span>18</span><span>19</span><span>20</span><span>21</span><span>22</span><span>23</span><span>24</span><span>25</span><span>26</span><span>27</span><span>28</span><span>29</span><span>30</span><span>31</span></div>
</div>

<div class="month-name teal" style="left:122px;top:993px;width:118px">September</div>
<div class="month" style="left:86px;top:1005px;width:160px;height:125px;padding-top:28px">
  <div class="weekdays"><span class="sun">sun</span><span>mon</span><span>tue</span><span>wed</span><span>thu</span><span>fri</span><span class="sat">sat</span></div>
  <div class="days"><span></span><span></span><span>1</span><span>2</span><span>3</span><span>4</span><span>5</span><span>6</span><span>7</span><span>8</span><span>9</span><span>10</span><span>11</span><span>12</span><span>13</span><span>14</span><span>15</span><span>16</span><span>17</span><span>18</span><span>19</span><span>20</span><span>21</span><span>22</span><span>23</span><span>24</span><span>25</span><span>26</span><span>27</span><span>28</span><span>29</span><span>30</span></div>
</div>

<div class="month-name teal" style="left:300px;top:993px;width:110px">October</div>
<div class="month" style="left:256px;top:1005px;width:160px;height:125px;padding-top:28px">
  <div class="weekdays"><span class="sun">sun</span><span>mon</span><span>tue</span><span>wed</span><span>thu</span><span>fri</span><span class="sat">sat</span></div>
  <div class="days"><span></span><span></span><span></span><span></span><span>1</span><span>2</span><span>3</span><span>4</span><span>5</span><span>6</span><span>7</span><span>8</span><span>9</span><span>10</span><span>11</span><span>12</span><span>13</span><span>14</span><span>15</span><span>16</span><span>17</span><span>18</span><span>19</span><span>20</span><span>21</span><span>22</span><span>23</span><span>24</span><span>25</span><span>26</span><span>27</span><span>28</span><span>29</span><span>30</span><span>31</span></div>
</div>

<div class="month-name teal" style="left:456px;top:987px;width:128px">November</div>
<div class="month" style="left:420px;top:1000px;width:165px;height:125px;padding-top:28px">
  <div class="weekdays"><span class="sun">sun</span><span>mon</span><span>tue</span><span>wed</span><span>thu</span><span>fri</span><span class="sat">sat</span></div>
  <div class="days"><span>1</span><span>2</span><span>3</span><span>4</span><span>5</span><span>6</span><span>7</span><span>8</span><span>9</span><span>10</span><span>11</span><span>12</span><span>13</span><span>14</span><span>15</span><span>16</span><span>17</span><span>18</span><span>19</span><span>20</span><span>21</span><span>22</span><span>23</span><span>24</span><span>25</span><span>26</span><span>27</span><span>28</span><span>29</span><span>30</span></div>
</div>

<div class="month-name purple" style="left:622px;top:1108px;width:120px">December</div>
<div class="month label-below" style="left:598px;top:998px;width:170px;height:118px">
  <div class="weekdays"><span class="sun">sun</span><span>mon</span><span>tue</span><span>wed</span><span>thu</span><span>fri</span><span class="sat">sat</span></div>
  <div class="days"><span></span><span></span><span>1</span><span>2</span><span>3</span><span>4</span><span>5</span><span>6</span><span>7</span><span>8</span><span>9</span><span>10</span><span>11</span><span>12</span><span>13</span><span>14</span><span>15</span><span>16</span><span>17</span><span>18</span><span>19</span><span>20</span><span>21</span><span>22</span><span>23</span><span>24</span><span>25</span><span>26</span><span>27</span><span>28</span><span>29</span><span>30</span><span>31</span></div>
</div>
</body>
</html>
```